Boutique Film/TV Company needs Business Card Design

Please see our website for background on our company and look of our current logo: www.morlandpictures.ca

Pantone 314U is our main colour.

Target Market(s)

Network of peers, funders and broadcasters.

Industry/Entity Type

Business

Requirements
Must have
• We would like rounded corners and the height of the card to be shorter than traditional (maybe?!)

It's important that we have room for our office address, office number, cell number, email address, website, facebook and linked-in info (though not all of us have a linked-in account).

Would like the logo to keep the exclamation marks over the letters but the tag line/tag words of "film - television - interactive" can stay or go or... surprise me!

Nice to have
• Silky matte finish.

We are open to a change in the font of our logo/name.

```html
<!DOCTYPE html>
<html lang="en">
<head>
<meta charset="utf-8">
<title>Morland Business Card</title>
<link rel="stylesheet" href="https://fonts.googleapis.com/css2?family=PT+Sans:wght@400;700&display=swap">
<style>
  :root {
    --brand-teal: #127a9a;
    --ink: #231f20;
    --paper: #ffffff;
    --backdrop: #e4e4e4;
    --card-w: 520px;
    --card-h: 324px;
  }
  * { margin: 0; padding: 0; box-sizing: border-box; }
  html, body { width: 1200px; height: 1000px; overflow: hidden; }
  body {
    background: var(--backdrop);
    font-family: "PT Sans", sans-serif;
    color: var(--ink);
    display: flex;
    align-items: center;
    justify-content: center;
    gap: 40px;
  }
  .card {
    position: relative;
    width: var(--card-w);
    height: var(--card-h);
    overflow: hidden;
    box-shadow: 0 2px 6px rgba(0,0,0,0.12);
  }

  /* Front */
  .card--front { background: var(--brand-teal); }
  .card--front .bubble {
    position: absolute;
    left: 45px;
    top: 56px;
    width: calc(100% - 45px);
    height: 160px;
  }
  .card--front .wordmark {
    position: absolute;
    left: 72px;
    top: 76px;
    font-size: 70px;
    font-weight: 400;
    line-height: 1;
    color: var(--ink);
    letter-spacing: 0.5px;
  }
  .card--front .tagline {
    position: absolute;
    left: 150px;
    top: 214px;
    font-size: 24px;
    font-weight: 700;
    color: var(--paper);
  }
  .card--front .website {
    position: absolute;
    right: 55px;
    top: 274px;
    font-size: 15px;
    color: var(--paper);
  }

  /* Back */
  .card--back { background: var(--paper); }
  .card--back .wordmark {
    position: absolute;
    left: 26px;
    top: 40px;
    font-size: 54px;
    font-weight: 400;
    line-height: 1;
    color: var(--ink);
  }
  .card--back .tagline {
    position: absolute;
    left: 26px;
    top: 106px;
    font-size: 13px;
    font-weight: 700;
    color: var(--brand-teal);
  }
  .card--back .person {
    position: absolute;
    left: 246px;
    top: 124px;
  }
  .person .name {
    font-size: 26px;
    font-weight: 700;
    color: var(--brand-teal);
    line-height: 1.1;
  }
  .person .position {
    font-size: 14px;
    font-weight: 700;
    color: var(--ink);
  }
  .contact {
    position: absolute;
    left: 246px;
    top: 192px;
    font-size: 11px;
    line-height: 13px;
  }
  .contact .group { margin-bottom: 9px; }
  .contact .row { display: flex; }
  .contact .label { width: 46px; color: var(--brand-teal); }
  .contact .value { color: var(--ink); }
</style>
</head>
<body>

  <section class="card card--front" aria-label="Card front">
    <svg class="bubble" viewBox="0 0 475 160" preserveAspectRatio="none" aria-hidden="true">
      <path d="M18 0 H475 V136 H100 L78 168 L74 136 H18 Q0 136 0 118 V18 Q0 0 18 0 Z" fill="#ffffff"/>
    </svg>
    <div class="wordmark">Morland</div>
    <div class="tagline">Films • Television • Interactive</div>
    <div class="website">www.morlandpictures.ca</div>
  </section>

  <section class="card card--back" aria-label="Card back">
    <div class="wordmark">Morland</div>
    <div class="tagline">Films • Television • Interactive</div>
    <div class="person">
      <div class="name">Name Surname</div>
      <div class="position">Position</div>
    </div>
    <div class="contact">
      <div class="group">
        <div class="row"><span class="label">Address</span><span class="value">#123 Lorem Street, Dolor sit City, PA 19017</span></div>
        <div class="row"><span class="label">Office</span><span class="value">610.555.0142</span></div>
      </div>
      <div class="group">
        <div class="row"><span class="label">Mobile</span><span class="value">237.555.0198</span></div>
        <div class="row"><span class="label">E-mail</span><span class="value">name@morlandpictures.ca</span></div>
        <div class="row"><span class="label">Facebook</span><span class="value">morlandpictures.facebook</span></div>
        <div class="row"><span class="label">Linked-In</span><span class="value">morlandpictures.linked-in</span></div>
      </div>
      <div class="group">
        <div class="row"><span class="label">Website</span><span class="value">www.morlandpictures.ca</span></div>
      </div>
    </div>
  </section>

</body>
</html>
```